Anselm business card

Business card for commercial photography , photographer specialized in advertising, architecture and interior photography, adventure imagery and camera work. 40 years old, worked for the last 20 years. Business card needs to convey a sense of confidence in work achieved. Card needs to be eye catching as will be left behind in many people's offices. Should also mention discreetly NLVG accredited photographer at the verso of the card. Phone number and website link must be apparent easily.

Target Market(s)

Advertising agencies, commercial photography representation

Industry/Entity Type

Architecture

Contact Information for Business Card

Phone number : +61 470 918 264
anselm.varnet@mailbrook.net
www.anselmvarnet.net

Font styles to use
Sans Serif

Requirements
Must have
• Email adress
• Website
• Phone number
• Name
• Photographer
Nice to have
• NLVG accredited photographer
Should not have
• Rond corners

```html
<!DOCTYPE html>
<html lang="en">
<head>
<meta charset="utf-8">
<title>Anselm Varnet — Business Card</title>
<link rel="stylesheet" href="https://fonts.googleapis.com/css2?family=Caveat:wght@600&family=Quicksand:wght@400;500&display=swap">
<style>
  :root {
    --backdrop: #e9e6e1;
    --front-light: #57534f;
    --front-dark: #231d1f;
    --accent-yellow: #f4e41c;
    --back-strong: #f8e816;
    --back-soft: #fbf39a;
    --ink-light: #f2f0ee;
    --ink-dark: #1e1c1c;
  }
  * { margin: 0; padding: 0; box-sizing: border-box; }
  html, body {
    width: 1200px; height: 1000px; overflow: hidden;
    background: var(--backdrop);
  }
  .stage {
    width: 1200px; height: 1000px;
    display: flex; flex-direction: column;
    align-items: center; justify-content: center; gap: 60px;
  }
  .card {
    position: relative;
    width: 700px; height: 400px;
    box-shadow: 0 10px 30px rgba(0,0,0,0.18);
  }
  .card--front {
    background: linear-gradient(135deg, var(--front-light) 0%, var(--front-dark) 70%);
  }
  .card--back {
    background: linear-gradient(200deg, var(--back-soft) 0%, var(--back-soft) 35%, var(--back-strong) 100%);
  }
  .corner {
    position: absolute; width: 44px; height: 44px;
    border: 0 solid var(--accent-yellow);
  }
  .corner--tl { top: 30px; left: 30px; border-top-width: 4px; border-left-width: 4px; }
  .corner--tr { top: 30px; right: 30px; border-top-width: 4px; border-right-width: 4px; }
  .corner--bl { bottom: 30px; left: 30px; border-bottom-width: 4px; border-left-width: 4px; }
  .corner--br { bottom: 30px; right: 30px; border-bottom-width: 4px; border-right-width: 4px; }
  .name {
    position: absolute; top: 122px; left: 0; right: 0;
    text-align: center;
    font-family: "Caveat", sans-serif; font-weight: 600;
    font-size: 84px; line-height: 1; letter-spacing: 2px;
    color: var(--accent-yellow);
  }
  .contact-line {
    position: absolute; top: 262px; left: 0; right: 0;
    display: flex; justify-content: center; gap: 34px;
    font-family: "Quicksand", sans-serif; font-weight: 400;
    font-size: 17px; color: var(--ink-light);
  }
  .icon-mark {
    position: absolute; top: 112px; left: 50%;
    width: 70px; height: 70px; margin-left: -35px;
    border: 4px solid var(--ink-dark);
  }
  .accreditation {
    position: absolute; top: 232px; left: 0; right: 0;
    text-align: center;
    font-family: "Quicksand", sans-serif; font-weight: 500;
    font-size: 30px; color: var(--ink-dark);
  }
</style>
</head>
<body>
<main class="stage">
  <section class="card card--front" aria-label="Card front">
    <span class="corner corner--tl"></span>
    <span class="corner corner--tr"></span>
    <span class="corner corner--bl"></span>
    <span class="corner corner--br"></span>
    <h1 class="name">Anselm Varnet</h1>
    <p class="contact-line">
      <span class="phone">+61 470 918 264</span>
      <span class="email">anselm.varnet@mailbrook.net</span>
      <span class="website">www.anselmvarnet.net</span>
    </p>
  </section>

  <section class="card card--back" aria-label="Card back">
    <span class="icon-mark" aria-hidden="true"></span>
    <p class="accreditation">NLVG accredited photographer</p>
  </section>
</main>
</body>
</html>
```